KAPT Mailer for Copper Vale Repair

We need an KAPT sized postcard for our auto repair business promoting that we now offer free pick up and delivery of vehicles in the Solanco area as well as free loaner vehicles. Our logo, and a copy of our current post card are attached for reference. Please promote the business in general and highlight the pick up drop off loaner service that is new.

```html
<!DOCTYPE html>
<html lang="en">
<head>
<meta charset="utf-8">
<title>Copper Vale Repair – KAPT Mailer</title>
<link href="https://fonts.googleapis.com/css2?family=Poppins:ital,wght@0,400;0,500;0,600;1,700&family=Russo+One&family=Mrs+Saint+Delafield&display=swap" rel="stylesheet">
<style>
:root{
  --stage:#333333;
  --paper:#ffffff;
  --ink:#111111;
  --green:#8ab846;
  --blue:#5fc6f1;
  --shadow-band:#dcdcdc;
  --chrome:#c9cdd1;
  --map:#d2f5e0;
  --photo-a:#d9dde0;
  --photo-b:#6d7278;
}
*{box-sizing:border-box;margin:0;padding:0}
html,body{width:849px;height:1200px;overflow:hidden;background:var(--stage)}
body{position:relative;font-family:'Poppins',sans-serif;color:var(--ink)}
.card{position:absolute;left:82px;width:685px;height:504px;background:var(--paper);overflow:hidden}
.card--front{top:83px}
.card--back{top:613px}
.abs{position:absolute}

/* shared */
.display{font-family:'Russo One',sans-serif;line-height:1;white-space:nowrap}
.script{font-family:'Mrs Saint Delafield',cursive;line-height:1;white-space:nowrap}
.wrench{position:absolute;height:16px;border-radius:8px;background:linear-gradient(180deg,#f1f3f5,var(--chrome) 55%,#9aa0a6);box-shadow:4px 6px 8px rgba(0,0,0,.18);transform-origin:0 50%}

/* front */
.brand{left:30px;top:48px;display:flex;align-items:center;gap:8px}
.brand__dot{width:16px;height:16px;border-radius:50%;background:var(--ink)}
.brand__name{font-weight:600;font-size:19px;line-height:1.05;color:var(--ink)}
.offer-shadow{left:380px;top:28px;width:305px;height:71px;background:var(--shadow-band);clip-path:polygon(10% 0,100% 0,100% 100%,0 100%)}
.offer{left:392px;top:36px;width:293px;height:55px;background:var(--green);clip-path:polygon(8% 0,100% 0,100% 100%,0 100%)}
.offer__text{right:44px;top:40px;text-align:right;font-weight:500;font-size:19.5px;line-height:23px;color:var(--ink)}
.amp-inline{font-family:'Mrs Saint Delafield',cursive;color:var(--paper);font-size:26px}
.tagline{left:164px;top:117px;font-size:44px;color:var(--ink)}
.headline-auto{left:32px;top:160px;font-size:86px;letter-spacing:-1px}
.headline-repair{left:36px;top:232px;font-size:91px;letter-spacing:-4px}
.amp-big{left:42px;top:272px;font-size:118px;color:var(--green)}
.subline{left:126px;top:307px;font-weight:500;font-size:30px;line-height:29px}
.photo-frame{left:330px;top:181px;width:355px;height:323px;background:var(--shadow-band);clip-path:polygon(78% 0,100% 0,100% 100%,0 100%)}
.photo{left:350px;top:189px;width:335px;height:315px;background:linear-gradient(150deg,var(--photo-a),var(--photo-b) 70%,#8a2a2a);clip-path:polygon(72% 0,100% 0,100% 100%,0 100%)}
.info-shadow{left:0;top:400px;width:330px;height:67px;background:var(--shadow-band)}
.info{left:0;top:408px;width:320px;height:52px;background:var(--blue)}
.info__row{left:30px;display:flex;align-items:center;gap:9px;font-size:11.6px}
.call{left:282px;top:389px;width:234px;height:96px;background:var(--green);border-radius:16px;transform:skewX(-22deg);transform-origin:0 100%}
.call__label{left:318px;top:401px;width:200px;text-align:center;font-family:'Russo One',sans-serif;font-style:italic;font-size:27px;transform:skewX(-12deg)}
.call__phone{left:308px;top:435px;width:210px;text-align:center;font-family:'Russo One',sans-serif;font-size:25px;color:var(--paper);transform:skewX(-12deg);letter-spacing:-1px}

/* back */
.script-complete{left:58px;top:28px;font-size:64px;color:var(--green)}
.headline-car{left:42px;top:74px;font-size:86px;letter-spacing:-2px}
.headline-care{left:40px;top:144px;font-size:106px;letter-spacing:-4px;color:var(--green)}
.services-shadow{left:0;top:246px;width:325px;height:44px;background:var(--shadow-band)}
.services{left:0;top:251px;width:320px;height:34px;background:var(--blue)}
.services__text{left:38px;top:259px;font-weight:700;font-style:italic;font-size:12.4px;letter-spacing:.1px}
.pitch{left:38px;top:304px;width:310px;font-size:11.2px;line-height:13.4px}
.perk{display:flex;gap:8px;font-size:11.4px;line-height:14.5px;top:392px}
.perk--left{left:38px}
.perk--right{left:236px}
.perk svg{flex:none;margin-top:2px}
.contact-shadow{left:0;top:441px;width:365px;height:45px;background:var(--shadow-band)}
.contact{left:0;top:446px;width:360px;height:35px;background:var(--green);display:flex;align-items:center;padding-left:40px;gap:8px;color:var(--paper);font-size:13px}
.contact__divider{width:1px;height:14px;background:var(--paper);margin:0 12px}
.return{left:400px;top:36px;display:flex;gap:5px;font-size:10.6px;line-height:15.4px}
.postage-divider{left:555px;top:38px;width:1px;height:53px;background:var(--ink)}
.postage{left:571px;top:36px;font-size:10.6px;line-height:15.4px}
.mailing-shadow{left:383px;top:101px;width:302px;height:45px;background:var(--shadow-band)}
.mailing{left:387px;top:106px;width:298px;height:34px;background:var(--blue)}
.mailing__text{left:415px;top:108px;font-size:11px;line-height:13.5px}
.map-frame{left:397px;top:177px;width:280px;height:327px;background:var(--shadow-band)}
.map{left:405px;top:185px;width:280px;height:319px;background:var(--map)}
</style>
</head>
<body>

<section class="card card--front" aria-label="Mailer front">
  <div class="abs brand">
    <span class="brand__dot"></span>
    <span class="brand__name">COPPER VALE<br>REPAIR</span>
  </div>

  <div class="wrench" role="img" aria-label="Chrome combination wrench" style="left:302px;top:97px;width:166px;transform:rotate(-35deg)"></div>

  <div class="abs offer-shadow"></div>
  <div class="abs offer"></div>
  <p class="abs offer__text">Free vehicle pick up,<br>drop off, <span class="amp-inline">&amp;</span> loaners</p>

  <p class="abs script tagline">High-quality</p>
  <h1 class="abs display headline-auto">AUTO</h1>
  <p class="abs display headline-repair">REPAIR</p>

  <div class="wrench" role="img" aria-label="Chrome combination wrench" style="left:321px;top:171px;width:182px;transform:rotate(35deg)"></div>

  <span class="abs script amp-big">&amp;</span>
  <p class="abs subline">preventative<br>maintenance!</p>

  <div class="abs photo-frame"></div>
  <div class="abs photo" role="img" aria-label="Photo of a mechanic working under the open hood of a white car in a workshop, with a red tool tray in front"></div>

  <div class="abs info-shadow"></div>
  <div class="abs info"></div>
  <div class="abs info__row" style="top:417px">
    <svg width="11" height="13" viewBox="0 0 11 13"><path d="M5.5 0A5.5 5.5 0 0 0 0 5.5C0 9 5.5 13 5.5 13S11 9 11 5.5A5.5 5.5 0 0 0 5.5 0Zm0 7.6a2.1 2.1 0 1 1 0-4.2 2.1 2.1 0 0 1 0 4.2Z" fill="#111"/></svg>
    <span>218 Millbrook Road, Unit D, Alder Ridge</span>
  </div>
  <div class="abs info__row" style="top:435px">
    <svg width="11" height="13" viewBox="0 0 11 13"><path d="M1 0l9 7.5-4 .3 2.4 4.4-1.6.8L4.4 8.6 1 11.5Z" fill="#111"/></svg>
    <span>CopperValeRepair.com</span>
  </div>

  <div class="abs call"></div>
  <p class="abs call__label">CALL US</p>
  <p class="abs call__phone">717-555-0148</p>
</section>

<section class="card card--back" aria-label="Mailer back">
  <p class="abs script script-complete">Complete</p>
  <h2 class="abs display headline-car">CAR</h2>
  <p class="abs display headline-care">CARE</p>

  <div class="wrench" role="img" aria-label="Chrome combination wrench" style="left:240px;top:-4px;width:185px;transform:rotate(38deg)"></div>

  <div class="abs services-shadow"></div>
  <div class="abs services"></div>
  <p class="abs services__text">INCLUDING INSPECTIONS AND EMISSIONS</p>

  <p class="abs pitch">Don't trust your car to just any automotive repair shop. We have the reliable, experienced technicians to quickly diagnose what's wrong &amp; fix it right the first time—saving you time, headaches &amp; money.</p>

  <div class="abs perk perk--left">
    <svg width="11" height="10" viewBox="0 0 11 10"><rect x="0" y="2" width="11" height="8" fill="#8ab846"/><rect x="3" y="0" width="5" height="3" fill="#8ab846"/></svg>
    <span>Trust in a timely, full-service<br>repair facility.</span>
  </div>
  <div class="abs perk perk--right">
    <svg width="11" height="10" viewBox="0 0 11 10"><path d="M1 9.5 4 3l3 3.5L10 .5" stroke="#8ab846" stroke-width="2" fill="none"/></svg>
    <span>Enjoy unparalleled<br>customer service</span>
  </div>

  <div class="abs contact-shadow"></div>
  <div class="abs contact">
    <svg width="13" height="13" viewBox="0 0 13 13"><path d="M2.6 0 5 2.8 3.6 4.5a8 8 0 0 0 4.9 4.9L10.2 8 13 10.4 11.3 13C5 12.6.4 8 0 1.7Z" fill="#fff"/></svg>
    <span>717-555-0148</span>
    <span class="contact__divider"></span>
    <svg width="11" height="13" viewBox="0 0 11 13"><path d="M1 0l9 7.5-4 .3 2.4 4.4-1.6.8L4.4 8.6 1 11.5Z" fill="#fff"/></svg>
    <span>CopperValeRepair.com</span>
  </div>

  <div class="abs return">
    <svg width="8" height="10" viewBox="0 0 11 13" style="margin-top:2px"><path d="M5.5 0A5.5 5.5 0 0 0 0 5.5C0 9 5.5 13 5.5 13S11 9 11 5.5A5.5 5.5 0 0 0 5.5 0Zm0 7.6a2.1 2.1 0 1 1 0-4.2 2.1 2.1 0 0 1 0 4.2Z" fill="#8ab846"/></svg>
    <p>Copper Vale Repair 218<br>Millbrook Road, Unit D<br>Alder Ridge, PA 17500</p>
  </div>
  <div class="abs postage-divider"></div>
  <p class="abs postage">PRSRT STD<br>ECRWSS<br>U.S.POSTAGE<br>PAID KAPT RETAIL</p>

  <div class="abs mailing-shadow"></div>
  <div class="abs mailing"></div>
  <p class="abs mailing__text">****************ECRWSS****KAPT<br>Local Postal Customer.</p>

  <div class="abs map-frame"></div>
  <div class="abs map" role="img" aria-label="Street map showing the shop location marked with a pin near the main road"></div>
</section>

</body>
</html>
```